CITRINE HARBOR, TROPICAL RECOVERY WATER

The project is to design a 12 ounce slim can label (it will be printed on the can, think gryphonix can" for a flavored water drink called "Citrine Harbor" or "Lumora-zen Water" with the tag line, "Tropical Recovery Water". The can logo should use a beach, with a mango sitting on a small table, or a basket of mangos on a small table. Another idea is to have a mango with sunglasses on, yes, sunglasses on the mango, and the beach and palm trees behind it. The label will need to include a generic NQB approved ingredient section, and a generic address as required. Thinking blue, yellows, and orange tones, with a white label or print. If there is a way to tastefully incorporate the label and required areas on a the silver can (ie no background), please have at it.

Target Market(s)

Coffee Drinkers, Juice Drinkers, Breakfast eaters, Bagel shop visitors

Font styles to use
Sans Serif

Colors
86cfc6
33b8a4
33a6d7
85cae6
fbf289
fbee3e
fee18a
fece3e

Requirements
Must have
• Marketing is everything on this project. The label must stand out in a sea of drink labels in a retail cooler or down a drink aisle in the grocery store.
Nice to have
• Modern, yet island feel. The beach setting, with the mango, can be a logo centered in the center of a silver can, or can be a landscape which takes up the total area of the can. Think mango water similar to cork lane meets gryphon ix, meets the beach and islands, but no fizz, just water to rehydrate.

```html
<!DOCTYPE html>
<html lang="en">
<head>
<meta charset="utf-8">
<title>Citrine Harbor – Tropical Recovery Water</title>
<link rel="stylesheet" href="https://fonts.googleapis.com/css2?family=Josefin+Sans:wght@600;700&family=Oswald:wght@400;500&display=swap">
<style>
  :root {
    --stage: #e9f3f1;
    --navy: #2f2a8f;
    --orange: #f79a2e;
    --orange-deep: #f58a24;
    --yellow: #fbe21c;
    --cream: #fff6c9;
    --sky: #85cae6;
    --sea: #33a6d7;
    --white: #ffffff;
    --panel: rgba(255, 255, 255, 0.88);
  }
  * { box-sizing: border-box; margin: 0; padding: 0; }
  html, body {
    width: 1084px;
    height: 1200px;
    overflow: hidden;
    background: var(--stage);
  }
  .canvas {
    position: relative;
    width: 1084px;
    height: 1200px;
    display: flex;
    align-items: center;
    justify-content: center;
  }
  .can-label {
    position: relative;
    width: 680px;
    height: 1120px;
    overflow: hidden;
    background: linear-gradient(180deg,
      var(--orange-deep) 0%,
      var(--orange) 20%,
      #fbb62c 38%,
      var(--yellow) 54%,
      var(--cream) 63%,
      var(--sky) 71%,
      #cfe9f5 88%,
      var(--white) 100%);
  }
  .beach-mark {
    position: absolute;
    top: 100px;
    left: 140px;
    width: 400px;
    height: 160px;
    border-radius: 80px 80px 12px 12px;
    background: linear-gradient(180deg, #f9b64a 0%, #f6a23a 60%, #8fc6e8 100%);
  }
  .brand-name {
    position: absolute;
    top: 278px;
    left: 0;
    width: 100%;
    text-align: center;
    font-family: "Josefin Sans", "Century Gothic", sans-serif;
    font-weight: 700;
    color: var(--navy);
    line-height: 1;
  }
  .brand-name .line-one { display: block; font-size: 74px; }
  .brand-name .line-two { display: block; font-size: 100px; margin-top: 6px; }
  .sun-rings {
    position: absolute;
    top: 500px;
    left: 150px;
    width: 380px;
    height: 380px;
  }
  .mascot {
    position: absolute;
    top: 590px;
    left: 250px;
    width: 180px;
    height: 210px;
    border-radius: 50% 50% 46% 46%;
    background: radial-gradient(circle at 45% 40%, #ffc93a 0%, var(--orange) 75%);
  }
  .tagline {
    position: absolute;
    top: 896px;
    left: 0;
    width: 100%;
    text-align: center;
    font-family: "Oswald", "Arial Narrow", sans-serif;
    font-weight: 500;
    color: var(--navy);
    line-height: 1;
  }
  .tagline .descriptor { display: block; font-size: 50px; letter-spacing: 1px; }
  .tagline .product-type {
    display: flex;
    align-items: center;
    justify-content: center;
    gap: 16px;
    font-size: 68px;
    margin-top: 8px;
    letter-spacing: 2px;
  }
  .wave-icon { width: 78px; height: 32px; }
  .label-facts {
    position: absolute;
    left: 60px;
    right: 60px;
    bottom: 16px;
    padding: 8px 14px;
    border-radius: 10px;
    background: var(--panel);
    font-family: "Oswald", "Arial Narrow", sans-serif;
    font-weight: 400;
    font-size: 13px;
    line-height: 1.35;
    color: var(--navy);
    text-align: center;
  }
  .label-facts strong { font-weight: 500; }
</style>
</head>
<body>
  <main class="canvas">
    <section class="can-label">
      <div class="beach-mark" role="img" aria-label="Beach illustration with clouds, sea waves and a parasol"></div>

      <h1 class="brand-name">
        <span class="line-one">Citrine</span>
        <span class="line-two">Harbor</span>
      </h1>

      <svg class="sun-rings" viewBox="0 0 380 380" aria-hidden="true">
        <g fill="none" stroke="#ffffff" stroke-opacity="0.7" stroke-width="2">
          <circle cx="190" cy="190" r="120"/>
          <circle cx="190" cy="190" r="140"/>
          <circle cx="190" cy="190" r="157"/>
          <circle cx="190" cy="190" r="172"/>
          <circle cx="190" cy="190" r="186"/>
        </g>
      </svg>

      <div class="mascot" role="img" aria-label="Cartoon mango character wearing pink sunglasses"></div>

      <p class="tagline">
        <span class="descriptor">TROPICAL RECOVERY</span>
        <span class="product-type">
          <svg class="wave-icon" viewBox="0 0 80 34" aria-hidden="true">
            <g fill="none" stroke="#2f2a8f" stroke-width="6" stroke-linecap="round">
              <path d="M4 12 Q14 2 24 12 T44 12 T64 12 T76 8"/>
              <path d="M4 26 Q14 16 24 26 T44 26 T64 26 T76 22"/>
            </g>
          </svg>
          WATER
          <svg class="wave-icon" viewBox="0 0 80 34" aria-hidden="true">
            <g fill="none" stroke="#2f2a8f" stroke-width="6" stroke-linecap="round">
              <path d="M4 12 Q14 2 24 12 T44 12 T64 12 T76 8"/>
              <path d="M4 26 Q14 16 24 26 T44 26 T64 26 T76 22"/>
            </g>
          </svg>
        </span>
      </p>

      <footer class="label-facts">
        <p><strong>Ingredients:</strong> Purified water, natural mango flavor, citric acid, sea salt, potassium citrate. NQB approved. 12 FL OZ (355 mL)</p>
        <p>Citrine Harbor Beverage Co., 42 Lagoon Way, Port Alder, CA 90000</p>
      </footer>
    </section>
  </main>
</body>
</html>
```